Business Card Design Project 4 Construction Business

I am after a creative, but sleek and simple/ clean business card design. This design will form the basis of future items and might include a logo or simply a creative way to lay out the text of my company name 'kestrel ventures'
I like the simplicity of black and white however I would also be happy to see a splash of colour introduced somehow to give the text some interest and make it stand out.
I would like a double sided card.
I am young (ish!) and professional, offering construction and project management services, what I don't want is the traditional builders type card featuring a cheesy hammer/ saw image etc.
As the company name, kestrel ventures, suggests, we focus on working closely and collaboratively together, in synergy with all stakeholders involved in the projects that we undertake
Construction

```html
<!DOCTYPE html>
<html lang="en">
<head>
<meta charset="utf-8">
<title>Kestrel Ventures – Business Card</title>
<link href="https://fonts.googleapis.com/css2?family=Michroma&family=Open+Sans:wght@400&display=swap" rel="stylesheet">
<style>
  :root {
    --backdrop: #9c9c9c;
    --brand-blue: #1996c8;
    --charcoal: #4a4a4c;
    --paper: #f4f4f2;
    --ink: #3a3a3a;
    --rule: #8a8a8a;
  }
  * { box-sizing: border-box; margin: 0; padding: 0; }
  html, body { width: 1200px; height: 720px; overflow: hidden; }
  body {
    background: var(--backdrop);
    display: flex;
    align-items: center;
    justify-content: center;
    gap: 40px;
    font-family: "Open Sans", sans-serif;
  }
  .card {
    position: relative;
    width: 550px;
    height: 314px;
    box-shadow: 0 6px 18px rgba(0,0,0,.25);
  }

  /* Front side */
  .card--front {
    background: var(--brand-blue);
    display: flex;
    align-items: center;
    justify-content: center;
  }
  .wordmark {
    font-family: "Michroma", sans-serif;
    text-transform: uppercase;
    line-height: 1.15;
  }
  .card--front .wordmark {
    color: #fff;
    font-size: 34px;
    letter-spacing: 2px;
    text-align: left;
  }
  .card--front .wordmark .line-2 { display: block; padding-left: 40px; font-size: 26px; letter-spacing: 6px; }

  /* Back side */
  .card--back { background: var(--paper); color: var(--ink); }
  .holder {
    position: absolute;
    top: 30px; left: 26px;
  }
  .holder__name {
    display: flex; align-items: center; gap: 10px;
    font-family: "Michroma", sans-serif;
    font-size: 20px;
    color: var(--brand-blue);
    letter-spacing: 1px;
  }
  .holder__name::before {
    content: ""; width: 14px; height: 14px; background: var(--charcoal);
  }
  .holder__meta {
    display: flex; align-items: flex-start;
    margin-top: 4px; padding-left: 90px;
    font-size: 12px;
  }
  .holder__phone {
    display: flex; align-items: center; gap: 5px;
    padding-right: 8px; border-right: 1px solid var(--rule);
    padding-bottom: 8px;
  }
  .holder__role { padding-left: 8px; padding-top: 14px; }

  .card--back .wordmark {
    position: absolute; top: 112px; right: 26px;
    color: var(--charcoal);
    font-size: 16px; letter-spacing: 1px;
    display: flex; align-items: center; gap: 10px;
  }
  .card--back .wordmark::before {
    content: ""; width: 16px; height: 16px; background: var(--brand-blue);
  }

  .emblem-block {
    position: absolute; left: 60px; top: 140px;
    width: 110px; height: 110px;
    background: var(--charcoal);
  }
  .divider {
    position: absolute; left: 232px; top: 140px;
    width: 1px; height: 150px; background: var(--rule);
  }
  .contact {
    position: absolute; left: 250px; top: 170px;
    list-style: none;
    font-size: 13px; line-height: 1.25;
  }
  .contact li { display: flex; align-items: flex-start; gap: 8px; }
  .contact svg { width: 11px; height: 11px; margin-top: 3px; flex: none; fill: var(--ink); }
</style>
</head>
<body>

  <section class="card card--front" aria-label="Card front">
    <div class="wordmark">Kestrel<span class="line-2">Ventures</span></div>
  </section>

  <section class="card card--back" aria-label="Card back">
    <div class="holder">
      <div class="holder__name">OWEN HARPER</div>
      <div class="holder__meta">
        <span class="holder__phone">
          <svg width="8" height="11" viewBox="0 0 8 11"><rect x=".5" y=".5" width="7" height="10" rx="1.5" fill="none" stroke="#3a3a3a"/></svg>
          0000-4172856
        </span>
        <span class="holder__role">Director</span>
      </div>
    </div>

    <div class="wordmark">Kestrel Ventures</div>

    <div class="emblem-block"></div>
    <div class="divider"></div>

    <ul class="contact">
      <li>
        <svg viewBox="0 0 12 12"><path d="M6 1 1 6h1.5v5h3V8h1v3h3V6H11z"/></svg>
        <span>FF-118, Elm Street<br>Portland, USA</span>
      </li>
      <li>
        <svg viewBox="0 0 12 12"><path d="M3 1 1.5 2.5c0 4 4 8 8 8L11 9 8.5 7 7 8C5.5 7.3 4.7 6.5 4 5l1-1.5z"/></svg>
        <span>0000000</span>
      </li>
      <li>
        <svg viewBox="0 0 12 12"><rect x="3" y="1" width="6" height="3"/><rect x="1" y="5" width="10" height="4"/><rect x="3" y="8" width="6" height="3"/></svg>
        <span>0000000</span>
      </li>
      <li>
        <svg viewBox="0 0 12 12"><path d="M1 2.5h10v7H1z" fill="none" stroke="#3a3a3a"/><path d="m1 2.5 5 4 5-4" fill="none" stroke="#3a3a3a"/></svg>
        <span>info@kestrelventures.com</span>
      </li>
      <li>
        <svg viewBox="0 0 12 12"><circle cx="6" cy="6" r="5"/></svg>
        <span>www.kestrelventures.com</span>
      </li>
    </ul>
  </section>

</body>
</html>
```